Diesel Fitting/Mechanical Company Needs a new Business Card

We would like a new business card that showcases our logo and business information.

Industry/Entity Type

Business

Contact Information for Business Card

314 Wendale Street
PO Box 7581 MARLOWE RIDGE QLD 4818
Phone: 49312787 Fax: 49312688 Mobile: 0438915276 ABN: 63 519 087 342

Requirements
Must have
• The following email addresses:
• admin@tkservicing.com.au , sales@tkservicing.com.au , accounts@tkservicing.com.au , parts@tkservicing.com.au , office@tkservicing.com.au
• Also need to have the website: www.tkservicing.com.au

```html
<!DOCTYPE html>
<html lang="en">
<head>
<meta charset="utf-8">
<title>TK Diesel Servicing — Business Card</title>
<link rel="stylesheet" href="https://fonts.googleapis.com/css2?family=Montserrat:wght@300;400;600&family=Work+Sans:wght@400&display=swap">
<style>
  :root {
    --backdrop: #5d5b5c;
    --card-orange: #f27324;
    --panel-white: #ffffff;
    --ink-dark: #1c1c1c;
    --ink-grey: #555555;
    --text-light: #ffffff;
  }
  * { box-sizing: border-box; margin: 0; padding: 0; }
  html, body {
    width: 1200px; height: 1000px; overflow: hidden;
    background: var(--backdrop);
  }
  .stage { position: relative; width: 1200px; height: 1000px; }
  .card {
    position: absolute; left: 295px; width: 587px; height: 335px;
    background: var(--card-orange); overflow: hidden;
  }
  .card--front { top: 149px; }
  .card--back { top: 517px; }

  .contact-list {
    position: absolute; left: 36px;
    font-family: "Montserrat", sans-serif; font-size: 13px; font-weight: 400;
    color: var(--text-light); line-height: 18.6px;
  }
  .contact-list--numbers { top: 36px; }
  .contact-list .label { font-weight: 600; }
  .contact-list--emails { top: 186px; line-height: 20px; font-weight: 300; }
  .emails-heading { font-weight: 600; font-size: 14px; margin-bottom: 6px; }

  .white-panel { position: absolute; inset: 0; }

  .brand {
    position: absolute; display: flex; align-items: center; gap: 10px;
    font-family: "Montserrat", sans-serif; font-weight: 600;
  }
  .brand__dot {
    width: 14px; height: 14px; border-radius: 50%; background: var(--ink-dark); flex: none;
  }
  .brand__name { color: var(--ink-dark); line-height: 1.05; }
  .card--front .brand { left: 395px; top: 140px; }
  .card--front .brand__name { font-size: 20px; }
  .card--back .brand { left: 50%; top: 50%; transform: translate(-50%, -50%); gap: 16px; }
  .card--back .brand__dot { width: 24px; height: 24px; }
  .card--back .brand__name { font-size: 34px; white-space: nowrap; }

  .address {
    position: absolute; left: 386px; top: 259px;
    font-family: "Work Sans", sans-serif; font-size: 13px;
    letter-spacing: 0.9px; line-height: 15.5px; color: var(--ink-grey);
  }
</style>
</head>
<body>
<main class="stage">
  <section class="card card--front">
    <svg class="white-panel" width="587" height="335" viewBox="0 0 587 335" aria-hidden="true">
      <path d="M290 335 C 275 250, 280 130, 330 60 C 370 10, 430 -10, 470 0 L 587 0 L 587 335 Z" fill="var(--panel-white)"/>
    </svg>
    <div class="contact-list contact-list--numbers">
      <p><span class="label">Phone:</span> 49312787</p>
      <p><span class="label">Fax:</span> 49312688</p>
      <p><span class="label">Mobile:</span> 0438915276</p>
      <p><span class="label">ABN:</span> 63 519 087 342</p>
      <p>www.tkservicing.com.au</p>
    </div>
    <div class="contact-list contact-list--emails">
      <p class="emails-heading">Emails:</p>
      <p>admin@tkservicing.com.au</p>
      <p>sales@tkservicing.com.au</p>
      <p>accounts@tkservicing.com.au</p>
      <p>parts@tkservicing.com.au</p>
      <p>office@tkservicing.com.au</p>
    </div>
    <div class="brand">
      <span class="brand__dot"></span>
      <span class="brand__name">TK Diesel<br>Servicing</span>
    </div>
    <p class="address">314 Wendale Street PO<br>Box 7581 MARLOWE<br>RIDGE QLD 4818</p>
  </section>

  <section class="card card--back">
    <div class="brand">
      <span class="brand__dot"></span>
      <span class="brand__name">TK Diesel Servicing</span>
    </div>
  </section>
</main>
</body>
</html>
```